Supplement Package and Bottle Design*

We are a supplement company rebranding a number of product ranges for which we need a designer.

We will start with two products for joint health supplementation that are part of one range.

1. DERMINOX K48 Internal Oil Drops
The internal oil drop requires a design for the outer box and inside bottle label – see attached.

Front of box should include the following text:
- DERMINOX K48
- Internal Oil Drops
- Original formula from the oils of fresh Laurus nobilis L. leaves and Curcuma longa L. rhizomes
- Dilute before use
- Food supplement
- 100ml
- Some prominent icon/ graphics indicating use for joint health
- Selunetra logo

2. DERMINOX R5 External Cream
The external cream only requires a design for the bottle label – see attached.
- DERMINOX R5
- External Cream
- Original formula from the oils of fresh Laurus nobilis L. leaves + 7 select ingredients
- 150ml
- Selunetra logo

Overall design:
- Common design between both products (oil drops and cream)
Must appeal to a customer base of middle-age/ seniors
- Pharmaceutical product feel with touch of nature/ herbal remedy
- Design my convey a feeling of dependability, trust, effectiveness
- Premium product feel. These are very expensive products
- Design must be easy to adapt for new product ranges
- Use icons/ symbols to indicate health application, example: icon of knee to indicate use for joints
- "K48" and "R5" should be prominent to distinguish the products
- You have a choice of two Selunetra logos. See attached.
- Primary colours: white and rgb(33, 136, 135)
- Designers can also consider some use of stamped gold/ silver for embellishments

Once a successful design/ feel has been chosen then exact dielines will be provided.

Target Market(s)

Seniors (65+ years old) with arthritis. Generally retired and affluent.

Industry/Entity Type

Health Product

Colors
33b8a4

Requirements
Must have
• As per project description.

Please creatively use a laurel wreath in the design. Either as a standalone element or multiple laurel wreaths in the background of the design. Can be vector or blended image.

As the supplements are made from bay leaves (laurel leaves) this subtle connection should be present.
Should not have
• Should not be cheap design and loud.

Premium design that conveys trust and pharmaceutical grade treatment with embellishments reminding that this is a natural/ herbal remedy product

```html
<!DOCTYPE html>
<html lang="en">
<head>
<meta charset="utf-8">
<title>DERMINOX K48 Internal Oil Drops – Box Front</title>
<link rel="stylesheet" href="https://fonts.googleapis.com/css2?family=Michroma&family=Lato:ital,wght@0,300;0,400;0,700;0,900;1,400&display=swap">
<style>
  :root {
    --teal: #2a9d86;
    --teal-deep: #1f8874;
    --silver: #c9cdd0;
    --white: #ffffff;
    --ink: #2b3b38;
    --stage: #e6e7e8;
  }
  * { margin: 0; padding: 0; box-sizing: border-box; }
  html, body { width: 1200px; height: 661px; overflow: hidden; }
  body {
    background: var(--stage);
    font-family: "Lato", sans-serif;
    display: flex; align-items: center; justify-content: center;
  }
  .box-front {
    position: relative;
    width: 280px; height: 600px;
    background: var(--white);
    box-shadow: 0 2px 10px rgba(0,0,0,0.08);
    overflow: hidden;
  }
  .panel-art { position: absolute; inset: 0; }
  .brand {
    position: absolute; top: 72px; left: 0; right: 0;
    display: flex; flex-direction: column; align-items: center; gap: 10px;
  }
  .brand-mark {
    width: 54px; height: 54px; border-radius: 50%;
    border: 2px solid var(--teal);
  }
  .brand-name {
    font-family: "Lato", sans-serif; font-weight: 400;
    font-size: 15px; letter-spacing: 4px; color: var(--teal);
  }
  .product-name {
    position: absolute; left: 18px; top: 258px;
    font-family: "Michroma", sans-serif; color: var(--white);
    font-size: 25px; line-height: 29px; letter-spacing: 0.5px;
  }
  .product-form {
    position: absolute; left: 20px; top: 322px;
    font-style: italic; font-size: 13px; color: var(--white);
  }
  .formula-intro {
    position: absolute; left: 22px; top: 368px;
    font-weight: 700; font-size: 13px; color: var(--white); white-space: nowrap;
  }
  .ingredients {
    position: absolute; left: 24px; top: 392px; width: 238px;
    background: var(--white); border-radius: 10px;
    padding: 4px 8px; text-align: center;
    font-weight: 900; font-size: 7.5px; line-height: 9px; color: var(--ink);
  }
  .joint-icon { position: absolute; left: 74px; top: 440px; width: 34px; height: 34px; }
  .herb-illustration {
    position: absolute; right: 0; top: 420px; width: 130px; height: 180px;
    background: linear-gradient(160deg, rgba(255,255,255,0.25), rgba(255,255,255,0.05));
  }
  .usage {
    position: absolute; left: 36px; top: 520px;
    font-weight: 700; font-size: 14px; color: var(--white);
  }
  .net-info {
    position: absolute; left: 52px; top: 564px; width: 110px;
    text-align: center; font-weight: 700; font-size: 9px; line-height: 12px; color: var(--white);
  }
</style>
</head>
<body>
  <main class="box-front">
    <svg class="panel-art" viewBox="0 0 280 600" width="280" height="600" aria-hidden="true">
      <defs>
        <linearGradient id="tealFill" x1="0" y1="0" x2="1" y2="1">
          <stop offset="0" stop-color="#2fa68e"/>
          <stop offset="1" stop-color="#1f8874"/>
        </linearGradient>
        <linearGradient id="silverEdge" x1="0" y1="0" x2="1" y2="0">
          <stop offset="0" stop-color="#e4e6e8"/>
          <stop offset="0.5" stop-color="#a9afb3"/>
          <stop offset="1" stop-color="#e4e6e8"/>
        </linearGradient>
      </defs>
      <path d="M0,246 C0,222 14,212 42,212 L150,212 C186,212 194,196 204,166 L222,98 C230,72 248,58 280,52 L280,600 L0,600 Z"
            fill="url(#silverEdge)" transform="translate(0,-6)"/>
      <path d="M0,246 C0,222 14,212 42,212 L150,212 C186,212 194,196 204,166 L222,98 C230,72 248,58 280,52 L280,600 L0,600 Z"
            fill="url(#tealFill)"/>
    </svg>

    <div class="brand">
      <span class="brand-mark"></span>
      <span class="brand-name">SELUNETRA</span>
    </div>

    <h1 class="product-name">DERMINOX<br>K48</h1>
    <p class="product-form">Internal Oil Drops</p>
    <p class="formula-intro">Original formula from the oils of:</p>
    <p class="ingredients">LAURUS NOBILIS L - LEAVES AND CURCUMA<br>LONGA L - RHIZOMES</p>

    <svg class="joint-icon" viewBox="0 0 34 34" aria-label="Joint health icon" role="img">
      <circle cx="17" cy="17" r="15" fill="none" stroke="#fff" stroke-width="1.6"/>
      <path d="M12,7 L15,15 M22,27 L19,19" stroke="#fff" stroke-width="2" stroke-linecap="round"/>
      <circle cx="17" cy="17" r="3.2" fill="none" stroke="#fff" stroke-width="1.6"/>
    </svg>

    <div class="herb-illustration" role="img" aria-label="Line illustration of laurel and turmeric leaves"></div>

    <p class="usage">Dilute before use</p>
    <p class="net-info">Food supplement<br>100ml</p>
  </main>
</body>
</html>
```